Business Card for Corinne Waldo

Name: Corinne Waldo
Title: Realtor
Email: Corinne@CorinneWaldoRE.example
Phone: 555-318-7492

On the front of the business card, I would like the photo, the contact information and the Corinne Waldo Logo. The backside is required to have the Broker logo and the required logos. Please use the colors from the logo design. Our company has a classy, professional look.

```html
<!DOCTYPE html>
<html lang="en">
<head>
<meta charset="utf-8">
<title>Corinne Waldo Business Card</title>
<link href="https://fonts.googleapis.com/css2?family=Cinzel:wght@500&family=Lato:wght@400&display=swap" rel="stylesheet">
<style>
  :root {
    --backdrop: #dcd7cf;
    --paper: #ffffff;
    --brand-red: #c0233f;
    --charcoal: #4b4a4f;
    --rule-dark: #3a393d;
    --photo-light: #9a9a9a;
    --photo-dark: #4e4e4e;
    --white: #ffffff;
  }
  * { margin: 0; padding: 0; box-sizing: border-box; }
  html, body { width: 1200px; height: 1000px; overflow: hidden; }
  body {
    background: var(--backdrop);
    position: relative;
    font-family: "Lato", sans-serif;
  }
  .card {
    position: absolute;
    top: 350px;
    width: 520px;
    height: 300px;
    overflow: hidden;
    box-shadow: 0 6px 18px rgba(0,0,0,0.12);
  }
  .card--front { left: 50px; background: var(--paper); }
  .card--back { left: 630px; background: var(--charcoal); }

  /* Brand lockup */
  .brand {
    position: absolute; display: flex; align-items: center; gap: 10px;
  }
  .brand__mark { flex: none; }
  .brand__text { display: flex; flex-direction: column; }
  .brand__name {
    font-family: "Cinzel", serif; font-weight: 500; white-space: nowrap;
    line-height: 1.05;
  }
  .brand__rule { height: 1.5px; margin: 3px 0 2px; }
  .brand__tagline {
    font-family: "Cinzel", serif; font-weight: 500; white-space: nowrap;
    align-self: flex-end; line-height: 1;
  }

  /* Front */
  .front-info {
    position: absolute; left: 0; top: 0; width: 300px; height: 300px;
  }
  .front-info .brand { left: 22px; top: 76px; }
  .front-info .brand__mark { width: 34px; height: 34px; background: var(--brand-red); }
  .front-info .brand__name { color: var(--brand-red); font-size: 23px; }
  .front-info .brand__rule { background: var(--rule-dark); }
  .front-info .brand__tagline { color: var(--brand-red); font-size: 10px; }
  .front-info .brand__title {
    font-family: "Lato", sans-serif; font-size: 11px; letter-spacing: 2px;
    text-transform: uppercase; color: var(--rule-dark); margin-top: 10px;
  }

  .contact-band {
    position: absolute; left: 0; bottom: 0; width: 300px; height: 92px;
    background: var(--brand-red);
    padding: 24px 0 0 24px;
    color: var(--white);
    font-size: 14px;
  }
  .contact-band__row { display: flex; align-items: center; gap: 9px; margin-bottom: 6px; white-space: nowrap; }
  .contact-band__row svg { width: 17px; height: 14px; flex: none; }

  .portrait {
    position: absolute; right: 0; top: 0; width: 220px; height: 300px;
    background: radial-gradient(ellipse at 50% 40%, var(--photo-light), var(--photo-dark) 85%);
  }

  /* Back */
  .card--back .brand { left: 100px; top: 92px; }
  .card--back .brand__mark { border: 2px solid var(--white); width: 44px; height: 44px; }
  .card--back .brand__name { color: var(--white); font-size: 28px; }
  .card--back .brand__rule { background: var(--white); }
  .card--back .brand__tagline { color: var(--white); font-size: 12px; }

  .affiliations {
    position: absolute; left: 100px; top: 190px;
    display: flex; align-items: center; gap: 14px;
  }
  .affiliations__broker {
    color: var(--white); font-family: "Cinzel", serif; font-weight: 500;
    font-size: 9px; letter-spacing: 0.5px; width: 64px; text-align: center;
    line-height: 1.3;
  }
  .badge { border: 2px solid var(--white); }
  .badge--housing { width: 38px; height: 38px; }
  .badge--realtor { width: 30px; height: 36px; }
  .badge--listing { width: 78px; height: 30px; }
</style>
</head>
<body>
  <section class="card card--front" aria-label="Business card front">
    <div class="front-info">
      <div class="brand">
        <span class="brand__mark"></span>
        <div class="brand__text">
          <span class="brand__name">Corinne Waldo</span>
          <span class="brand__rule"></span>
          <span class="brand__tagline">Real Estate</span>
          <span class="brand__title">Realtor</span>
        </div>
      </div>
      <div class="contact-band">
        <div class="contact-band__row">
          <svg viewBox="0 0 17 14" aria-hidden="true"><rect x="1" y="1" width="15" height="12" fill="none" stroke="#fff" stroke-width="1.5"/><path d="M1 1 L8.5 8 L16 1" fill="none" stroke="#fff" stroke-width="1.5"/></svg>
          <span>Corinne@CorinneWaldoRE.example</span>
        </div>
        <div class="contact-band__row">
          <svg viewBox="0 0 17 14" aria-hidden="true"><path d="M1 4 Q8.5 -1 16 4 L14 6 L11.5 4.5 L11.5 3 Q8.5 2 5.5 3 L5.5 4.5 L3 6 Z" fill="#fff"/><rect x="3" y="7" width="11" height="6" rx="1" fill="#fff"/></svg>
          <span>555-318-7492</span>
        </div>
      </div>
    </div>
    <div class="portrait" role="img" aria-label="Black and white portrait photo of the realtor"></div>
  </section>

  <section class="card card--back" aria-label="Business card back">
    <div class="brand">
      <span class="brand__mark"></span>
      <div class="brand__text">
        <span class="brand__name">Corinne Waldo</span>
        <span class="brand__rule"></span>
        <span class="brand__tagline">Real Estate</span>
      </div>
    </div>
    <div class="affiliations">
      <span class="affiliations__broker">Halvorsen Reed</span>
      <span class="badge badge--housing" role="img" aria-label="Equal housing badge"></span>
      <span class="badge badge--realtor" role="img" aria-label="Realtor membership badge"></span>
      <span class="badge badge--listing" role="img" aria-label="Listing service badge"></span>
    </div>
  </section>
</body>
</html>
```